Design the Marketing Brochure for a service company with Vantage 500 Clients

We need to redesign our marketing brochures to reflect the new service lines we have added in the last few years. We are a professional staffing firm based in Miami, Florida and have a portfolio of clients that include: Coral Meridian, Bluewave Voyage Lines, Patty Palace Corp, Horizon Lens Network Etc. I have attached our current marketing inserts in pdf format. I would like to have 5 inserts displaying our services, process and business lines.

Target Market(s)

Vantage 1000 companies. Within those companies our clients are: CFO's, VP of Finance, Controller, Head of Human Resources, Banking Executives etc. All financial related roles.

Industry/Entity Type

Recruitment

Colors
ec1f27
ffffff
aaaaaa
fece3e
000000

Requirements
Must have
• 5 pages 3 of which we have mots of the content. One page dedicated to " Temporary Staffing" and one page dedicated to our "Banking Division" The brochures should include professional pictures and a well designed layout that looks professional and appealing to an educated client. Our colors are Red, Gray and White.
• Please see our attached brochures and our website at www.kvotalent.example
Nice to have
• Professional pictures of people in the business workplace.
Should not have
• Graphics or cartoons of any kind.

```html
<!DOCTYPE html>
<html lang="en">
<head>
<meta charset="utf-8">
<title>Temporary Staffing — Brochure Spread</title>
<link href="https://fonts.googleapis.com/css2?family=Open+Sans:wght@400;600;700;800&display=swap" rel="stylesheet">
<style>
:root{
  --red:#9e1c20;
  --yellow:#f6c534;
  --ink:#1d1d1d;
  --white:#ffffff;
  --paper:#d9cccd;
  --photo-top:#c9cfc3;
  --photo-bottom:#9fa19a;
}
*{box-sizing:border-box;margin:0;padding:0}
html,body{width:1200px;height:833px;overflow:hidden}
body{background:var(--paper);font-family:"Open Sans",Arial,sans-serif;color:var(--ink)}
.spread{position:absolute;left:30px;top:36px;width:1140px;height:760px;display:flex;box-shadow:0 10px 30px rgba(0,0,0,.25)}
.page{position:relative;width:570px;height:760px;overflow:hidden;background:var(--white)}
.page--left{background:linear-gradient(180deg,var(--photo-top),#b9bdb2 55%,var(--photo-bottom))}
.page-header{position:absolute;left:0;top:0;width:570px;height:170px}
.page-title{position:absolute;color:var(--white);font-weight:800;text-transform:uppercase;letter-spacing:.3px;line-height:1.1}
.page--left .page-title{left:28px;top:30px;font-size:24px}
.page--right .page-title{left:30px;top:24px;font-size:20px}
.hero-photo{position:absolute;left:312px;top:180px;width:240px;height:510px;border-radius:6px;background:linear-gradient(180deg,rgba(60,60,60,.22),rgba(40,40,40,.42))}
.intro{position:absolute;left:26px;top:168px;width:276px}
.label{display:inline-block;background:var(--yellow);color:var(--red);font-weight:700;padding:3px 14px 3px 10px;line-height:1.15;clip-path:polygon(0 0,100% 0,94% 100%,0 100%)}
.label--lg{font-size:14.5px}
.label--md{font-size:16px}
.intro p{font-size:10.5px;line-height:1.35;margin:6px 0 10px;color:#222}
.expertise{position:absolute;left:0;top:534px;width:302px;height:226px;background:var(--red);border-top:4px solid var(--ink);border-right:4px solid var(--ink);padding:0 14px 0 22px}
.expertise .label{margin-top:-14px;font-size:16px}
.expertise p{color:var(--white);font-size:10px;margin:8px 0 6px}
.expertise ul{list-style:none;columns:2;column-gap:10px}
.expertise li{color:var(--white);font-size:10px;line-height:1.3;padding-left:13px;position:relative;break-inside:avoid}
.expertise li::before{content:"";position:absolute;left:0;top:4px;width:6px;height:6px;border-radius:50%;background:var(--yellow)}
.body-copy{position:absolute;left:30px;width:510px;font-size:9.2px;line-height:1.32;color:#222}
.body-copy p{margin-bottom:6px}
.copy-top{top:136px}
.copy-mid{top:286px}
.copy-mid .label{margin-bottom:7px}
.office-photo{position:absolute;left:0;top:478px;width:270px;height:262px;background:linear-gradient(135deg,#d9dde2,#8e98a3 60%,#2f3540)}
.overworked{position:absolute;left:270px;top:466px;width:300px;height:274px;background:var(--red);border-top:4px solid var(--ink);border-left:4px solid var(--ink);padding:0 14px}
.overworked .label{margin-top:-12px;font-size:14px;margin-left:-4px}
.overworked p{color:var(--white);font-size:8.8px;line-height:1.3;margin-top:6px;text-align:justify}
.fold{position:absolute;left:568px;top:0;width:4px;height:760px;background:linear-gradient(90deg,rgba(0,0,0,.18),rgba(0,0,0,0))}
</style>
</head>
<body>
<main class="spread">
  <section class="page page--left">
    <div class="hero-photo" role="img" aria-label="Businessman standing on a ladder looking through binoculars into a misty landscape"></div>
    <svg class="page-header" viewBox="0 0 570 170" aria-hidden="true">
      <path d="M0 0H570V52Q350 62 150 122Q60 146 0 152Z" fill="var(--red)"/>
      <path d="M0 152Q60 146 150 122Q350 62 570 52V60Q350 71 150 131Q60 154 0 160Z" fill="var(--yellow)"/>
      <path d="M0 160Q60 154 150 131Q350 71 570 60V64Q350 76 150 136Q60 159 0 165Z" fill="var(--ink)"/>
    </svg>
    <h1 class="page-title">Temporary Staffing</h1>

    <div class="intro">
      <span class="label label--lg">Flexible Accounting Staffing Solutions</span>
      <p>You can hire highly skilled professionals from KVO Talent International in three different ways:</p>
      <span class="label label--md">Temporary:</span>
      <p>Supplement your full-time staff on a project basis. This staffing solution is effective when ongoing productivity and cost management are essential.</p>
      <span class="label label--md">Temporary-to-hire:</span>
      <p>Quickly staff a vacant position with the option to hire full time. This staffing solution is effective when you want to assess fit before you make a hiring decision.</p>
      <p>Staffing support for long-term projects. This staffing solution is effective for long-term or recurring projects that require a specialized skill set.</p>
    </div>

    <div class="expertise">
      <span class="label">Areas of Accounting<br>Staffing Expertise</span>
      <p>Here are just a few of our specialty areas:</p>
      <ul>
        <li>Accounting Clerk</li><li>Accounting Manager</li><li>Accounts Payable</li><li>Accounts Receivable</li>
        <li>Auditor</li><li>Billing</li><li>Bookkeeping</li><li>Cost Accounting</li><li>Credit &amp; Collections</li>
        <li>Data Entry Clerk</li><li>Financial Analyst</li><li>Financial Services</li><li>Payroll</li>
        <li>Senior Accountant</li><li>Staff Accountant</li><li>Tax Accounting</li>
      </ul>
    </div>
  </section>

  <section class="page page--right">
    <svg class="page-header" viewBox="0 0 570 170" aria-hidden="true">
      <path d="M0 0H570V62Q380 70 180 100Q70 114 0 118Z" fill="var(--red)"/>
      <path d="M0 118Q70 114 180 100Q380 70 570 62V70Q380 79 180 109Q70 122 0 126Z" fill="var(--yellow)"/>
      <path d="M0 126Q70 122 180 109Q380 79 570 70V74Q380 84 180 114Q70 127 0 130Z" fill="var(--ink)"/>
    </svg>
    <h2 class="page-title">Finance and Accounting Staffing<br>Professionals</h2>

    <div class="body-copy copy-top">
      <p>When you come to KVO Talent International with a staffing request, we will ask you to provide a job description, a list of skills you desire in a candidate, any qualifications unique to your organization and the length of time you anticipate needing the extra assistance. We will then match you with pre-evaluated finance and accounting professionals with the skills and experience required for your business needs.</p>
      <p>We want your experience with us to exceed your expectations of what it's like to work with staffing companies. We will listen to your needs and help you implement the best staffing services for your organization. If you are not satisfied, simply notify us within the first eight hours of the assignment. You will not be charged for those hours, and we will promptly send you a replacement.</p>
      <p>Speak with an accounting recruiter to discuss your temporary staffing needs or learn more about our services and guarantee.</p>
    </div>

    <div class="body-copy copy-mid">
      <span class="label label--md">When you're adjusting to an influx of new business</span>
      <p>New business is a good thing, right? It may not feel like it if you don't have the staff to take on the extra workload. In fact, new business could mean big headaches if your staff is already stressed or customers notice a drop in quality.</p>
      <p>A good course of action may be to contact temp staffing agencies serving your area for help during the transition. After all, finding highly skilled accounting professionals can be a time-consuming process, and if your hands are full with new business, you likely have none to spare.</p>
      <p>A good agency will evaluate a candidate's work history and conduct face-to-face interviews, assess software skills and conduct accounting knowledge evaluation tests. They'll also check a candidate's references, conduct quality assurance surveys and offer guarantees for your temporary team member. That way you know the job will get done right.</p>
    </div>

    <div class="office-photo" role="img" aria-label="Smiling young professional shaking hands across a desk in an office with binders"></div>

    <div class="overworked">
      <span class="label">When the team is overworked</span>
      <p>Has your staff been missing deadlines or arriving to work late? Before threatening to substitute this year's bonuses with alarm clocks, you need to assess the cause of these issues. It could be because they're overworked. Other warning signs of an unmanageable workload include team members who are suddenly making more mistakes than usual, workers who constantly call in sick and an increase in overtime hours.</p>
      <p>Give your staff some relief by bringing in support from temp staffing agencies. A temporary accounting professional can help you address your workplace's immediate needs. During that time, you'll have an opportunity to observe the temporary staff member's performance firsthand while you determine the longer-term needs of your organization. You may decide that you actually need to hire another full-time worker. And the temporary professional who's performed well on the job could be the ideal candidate for the role.</p>
    </div>
  </section>
  <div class="fold" aria-hidden="true"></div>
</main>
</body>
</html>
```